Larkspur Homes - wanted BRILLIANT website design for our new property investing company

We need a website design for our new company based in Bristol, England, UK called "Larkspur Homes". We help buy people property who are in financial difficulty or who are needing to sell their property quickly for reasons such as death, divorce/separation, relocation, emigration.

We have a logo being designed incorporating strawberry and property (so red and green). We would like designs to communicate an elegant ,professional, approachable, friendly
fresh clean but also warm appealing appearance
Not too busy
Website consistent with logo and company name i.e. colour scheme

Please use our word document for content as a guide but use professional judgement for minor alterations if you feel they would benefit the site/structure etc

Please ask at any time if not sure

Target Market(s)

Adult british population, those that have a mortgage / loan / own property

Industry/Entity Type

Financial

Font styles to use
Serif
Sans Serif
Decorative

Colors
0692cd
33b7a4
acd036
fbee3e
3176b5
886aae
a6479a
e567a6
eb1f27

Requirements
Must have
• This must not look like a template website we are looking for UNIQUE please!
Nice to have
• Bristol pictures instead of generic, or colourful line drawings/comic drawings of houses/property/keys/happy people.....
Should not have
• An obvious off the shelf template design

```html
<!DOCTYPE html>
<html lang="en">
<head>
<meta charset="utf-8">
<title>Larkspur Homes</title>
<link rel="stylesheet" href="https://fonts.googleapis.com/css2?family=Oswald:wght@500;700&family=Open+Sans:wght@300;400;600;700&display=swap">
<style>
:root{
  --red:#e2313a;
  --red-dark:#b7222a;
  --green:#6cb33f;
  --green-dark:#4f8f2a;
  --ink:#444;
  --muted:#8a8a8a;
  --grey-bg:#eeeeee;
  --footer:#1e1e1e;
  --footer-deep:#141414;
  --white:#fff;
}
*{box-sizing:border-box;margin:0;padding:0}
html,body{width:747px;height:1200px;overflow:hidden;background:var(--white)}
body{font-family:"Open Sans",Arial,sans-serif;color:var(--ink);position:relative}
.abs{position:absolute}
ul{list-style:none}

/* header */
.site-header{position:absolute;left:0;top:0;width:747px;height:62px;background:var(--white);border-bottom:3px solid var(--red)}
.brand{position:absolute;left:22px;top:14px;display:flex;align-items:center;gap:8px;font-weight:700;font-size:15px;color:var(--red)}
.brand-dot{width:26px;height:26px;border-radius:50%;background:var(--red)}
.top-contacts{position:absolute;right:20px;top:6px;font-size:9px;color:var(--muted);display:flex;gap:14px;align-items:center}
.top-contacts span{display:flex;align-items:center;gap:4px}
.main-nav{position:absolute;right:18px;top:30px;display:flex;font-size:10px}
.main-nav a{display:block;padding:8px 10px 9px;color:var(--ink);text-decoration:none;border-left:1px solid #ddd}
.main-nav a:first-child{border-left:0}
.main-nav a.active{background:var(--red);color:var(--white)}

/* hero */
.hero{position:absolute;left:0;top:62px;width:747px;height:310px}
.hero-photo{position:absolute;inset:0;background:linear-gradient(100deg,#2a211b 0%,#4b3b2f 40%,#8c7864 70%,#c7b7a0 100%)}
.hero-text{position:absolute;left:30px;top:78px;color:var(--white);font-family:"Oswald",sans-serif;text-transform:uppercase;line-height:1.05}
.hero-text .l1{font-size:34px;font-weight:700}
.hero-text .l2{font-size:40px;font-weight:700;color:var(--red)}
.hero-text .l2 em{font-style:normal;color:var(--white);font-size:28px}
.hero-text .l3{font-size:22px;font-weight:500}
.btn{display:inline-block;background:var(--green);color:var(--white);font-size:11px;font-weight:600;padding:7px 16px;border-radius:2px}
.hero .btn{position:absolute;left:30px;top:196px}
.contact-form{position:absolute;left:502px;top:22px;width:222px;height:262px;background:rgba(255,255,255,.92);box-shadow:0 2px 6px rgba(0,0,0,.3)}
.contact-form h3{background:var(--green);color:var(--white);font-size:12px;font-weight:600;text-align:center;padding:7px 0}
.field{margin:7px 10px 0;height:22px;border:1px solid #cfcfcf;background:var(--white);font-size:9px;color:var(--muted);padding:4px 6px 0 22px;position:relative}
.field svg{position:absolute;left:6px;top:5px}
.field.message{height:64px}
.send{margin:8px 10px 0;height:24px;background:#3a3a3a;color:var(--white);font-size:11px;font-weight:600;text-align:center;line-height:24px}

/* services */
.services{position:absolute;left:0;top:372px;width:747px;height:260px}
.services h2{position:absolute;left:0;width:747px;top:30px;text-align:center;font-weight:300;font-size:19px;color:var(--red)}
.services-image{position:absolute;left:96px;top:72px;width:220px;height:150px;background:radial-gradient(circle at 50% 45%,#c9c9c9,#8f8f8f 55%,#e8e8e8 100%)}
.services-body{position:absolute;left:372px;top:80px;width:320px}
.services-body h3{font-weight:400;font-size:13px;color:var(--red);margin-bottom:8px}
.services-body li{font-size:9.5px;color:var(--ink);line-height:16px;padding-left:12px;position:relative}
.services-body li::before{content:"";position:absolute;left:0;top:6px;width:5px;height:5px;border-radius:50%;background:var(--red)}
.services-body .btn{margin-top:10px}

/* opportunity */
.opportunity{position:absolute;left:0;top:632px;width:747px;height:252px;background:var(--grey-bg)}
.opportunity h2{position:absolute;left:28px;top:16px;font-weight:300;font-size:17px;color:var(--red)}
.room-photo{position:absolute;top:54px;width:216px;height:104px}
.room-photo.a{left:28px;background:linear-gradient(180deg,#6b5a48,#3b2f26)}
.room-photo.b{left:254px;background:linear-gradient(180deg,#e9e6e1,#a79f95)}
.opportunity p{position:absolute;left:28px;top:168px;width:442px;font-size:9px;line-height:13px;color:var(--ink)}
.opportunity .btn{position:absolute;left:28px;top:220px}
.help-panel{position:absolute;left:504px;top:634px;width:224px;height:270px;background:var(--red);color:var(--white);box-shadow:0 2px 6px rgba(0,0,0,.2)}
.help-panel h3{font-weight:400;font-size:18px;padding:14px 16px 10px}
.help-panel li{font-size:9px;padding:4px 16px;border-top:1px solid rgba(255,255,255,.25)}
.help-panel li.current{background:var(--red-dark)}

/* partners */
.partners{position:absolute;left:0;top:884px;width:747px;height:104px}
.partners h2{position:absolute;left:28px;top:30px;font-weight:300;font-size:19px;color:var(--red)}
.badges{position:absolute;left:175px;top:62px;display:flex;gap:36px;align-items:center}
.badge{width:100px;height:34px;background:#d7d7d7}
.badge.round{width:34px;height:34px;border-radius:50%}
.badge.navy{background:#243a6b}

/* footer */
.site-footer{position:absolute;left:0;top:988px;width:747px;height:212px;background:var(--footer);color:#bdbdbd;font-size:9px}
.footer-col{position:absolute;top:18px}
.footer-col h4{color:var(--white);font-size:11px;font-weight:600;margin-bottom:8px}
.footer-col li{line-height:14px}
.footer-col li.on{color:var(--red)}
.footer-col p{line-height:13px;margin-bottom:6px}
.contact-line{display:flex;align-items:center;gap:6px;margin-bottom:6px}
.social li{display:flex;align-items:center;gap:7px;margin-bottom:5px}
.social i{width:14px;height:14px;background:var(--red);display:block}
.copyright{position:absolute;left:0;bottom:0;width:747px;height:30px;background:var(--footer-deep);text-align:center;line-height:30px;font-size:8.5px;color:#888}
</style>
</head>
<body>

<header class="site-header">
  <div class="brand"><span class="brand-dot"></span>Larkspur Homes</div>
  <div class="top-contacts">
    <span><svg width="9" height="9" viewBox="0 0 10 10"><path d="M2 1l2 2-1 1.5c.8 1.5 1.5 2.2 3 3L7.5 6l2 2-1.5 1.5C4.5 9 1 5.5.5 2.5z" fill="#8a8a8a"/></svg>07700 900 123</span>
    <span><svg width="10" height="8" viewBox="0 0 10 8"><rect x=".5" y=".5" width="9" height="7" fill="none" stroke="#8a8a8a"/><path d="M.5.5l4.5 4 4.5-4" fill="none" stroke="#8a8a8a"/></svg>info@larkspur-homes.co.uk</span>
  </div>
  <nav class="main-nav">
    <a class="active">Sell Your Property Fast</a>
    <a>Rent Your Property Fast</a>
    <a>The 5 Easy Steps</a>
    <a>About Us</a>
    <a>Contact Us</a>
  </nav>
</header>

<section class="hero">
  <div class="hero-photo" role="img" aria-label="Photo of a bright modern bedroom with a made bed"></div>
  <div class="hero-text">
    <div class="l1">Do you want to</div>
    <div class="l2">Sell <em>or</em> Rent</div>
    <div class="l3">Out your house quickly?</div>
  </div>
  <span class="btn">Read More</span>
  <form class="contact-form">
    <h3>Contact Form</h3>
    <div class="field"><svg width="10" height="10" viewBox="0 0 10 10"><circle cx="5" cy="3" r="2.3" fill="#999"/><path d="M1 10c0-3 2-4.5 4-4.5S9 7 9 10z" fill="#999"/></svg>Name</div>
    <div class="field"><svg width="10" height="8" viewBox="0 0 10 8"><rect x=".5" y=".5" width="9" height="7" fill="none" stroke="#999"/><path d="M.5.5l4.5 4 4.5-4" fill="none" stroke="#999"/></svg>Email</div>
    <div class="field"><svg width="10" height="10" viewBox="0 0 10 10"><path d="M2 1l2 2-1 1.5c.8 1.5 1.5 2.2 3 3L7.5 6l2 2-1.5 1.5C4.5 9 1 5.5.5 2.5z" fill="#999"/></svg>Phone number</div>
    <div class="field"><svg width="10" height="10" viewBox="0 0 10 10"><path d="M5 .5a3.5 3.5 0 0 1 3.5 3.5C8.5 6.5 5 9.5 5 9.5S1.5 6.5 1.5 4A3.5 3.5 0 0 1 5 .5z" fill="#999"/></svg>Property address</div>
    <div class="field message"><svg width="10" height="10" viewBox="0 0 10 10"><path d="M1 1h8v6H4L2 9V7H1z" fill="#999"/></svg>Message</div>
    <div class="send">Send</div>
  </form>
</section>

<section class="services">
  <h2>We are a local family run property business who specialize in:</h2>
  <div class="services-image" role="img" aria-label="Illustration of hands holding a small model house"></div>
  <div class="services-body">
    <h3>We are a local family run property.</h3>
    <ul>
      <li>Buying properties quickly</li>
      <li>Finding creative solutions to your property problems</li>
      <li>Property rental management</li>
      <li>Lettings to professional and student tenants</li>
      <li>Guaranteed rent and management schemes for</li>
      <li>landlords</li>
    </ul>
    <span class="btn">View More</span>
  </div>
</section>

<section class="opportunity">
  <h2>Opportunity not to be missed</h2>
  <div class="room-photo a" role="img" aria-label="Photo of a warm living room interior"></div>
  <div class="room-photo b" role="img" aria-label="Photo of a bright modern lounge interior"></div>
  <p>It is a long established fact that a reader will be distracted by the readable content of a page when looking at its layout. The point of using sample text is that it has a more-or-less normal distribution of letters, as opposed to using placeholder copy, making it look like readable English. Many desktop publishing packages and web page editors now use sample text as their default model text.</p>
  <span class="btn">View More</span>
</section>

<aside class="help-panel">
  <h3>Who can we help</h3>
  <ul>
    <li>Home buy representatives</li>
    <li>Divorce or separation</li>
    <li>Financial problems</li>
    <li>Don't like estate agents?</li>
    <li>Property needing work</li>
    <li>Relocating abroad</li>
    <li>Problem tenants</li>
    <li class="current">Opportunity not to be missed</li>
    <li>Guaranteed rent scheme</li>
    <li>All Landlords</li>
    <li>Repossession and debt</li>
    <li>Inherited property sales</li>
  </ul>
</aside>

<section class="partners">
  <h2>Our Partners</h2>
  <div class="badges">
    <div class="badge round" role="img" aria-label="Partner badge"></div>
    <div class="badge navy" role="img" aria-label="Partner badge"></div>
    <div class="badge" role="img" aria-label="Partner badge"></div>
    <div class="badge round" role="img" aria-label="Partner badge"></div>
  </div>
</section>

<footer class="site-footer">
  <div class="footer-col" style="left:22px">
    <h4>Sitemap</h4>
    <ul>
      <li>Home</li>
      <li class="on">Sell Your Property</li>
      <li>Rent Your Property</li>
      <li>The 5 Easy Steps</li>
      <li>About Us</li>
      <li>Contact Us</li>
    </ul>
  </div>
  <div class="footer-col" style="left:200px;width:160px">
    <h4>Contact Us</h4>
    <p>A local family run team helping you sell or rent property.</p>
    <div class="contact-line"><svg width="9" height="8" viewBox="0 0 10 8"><rect x=".5" y=".5" width="9" height="7" fill="none" stroke="#bdbdbd"/><path d="M.5.5l4.5 4 4.5-4" fill="none" stroke="#bdbdbd"/></svg>info@larkspur-homes.co.uk</div>
    <div class="contact-line"><svg width="9" height="9" viewBox="0 0 10 10"><path d="M2 1l2 2-1 1.5c.8 1.5 1.5 2.2 3 3L7.5 6l2 2-1.5 1.5C4.5 9 1 5.5.5 2.5z" fill="#bdbdbd"/></svg>07700 900 123</div>
  </div>
  <div class="footer-col" style="left:392px;width:180px">
    <h4>About Us</h4>
    <p>We are a family run business based in Bristol, buying homes quickly and fairly for owners who need a fast, stress free sale.</p>
  </div>
  <div class="footer-col social" style="left:618px">
    <h4>Follow Us</h4>
    <ul>
      <li><i></i>Newsfeed</li>
      <li><i></i>Updates</li>
      <li><i></i>Circles</li>
      <li><i></i>Network</li>
    </ul>
  </div>
  <div class="copyright">2024 Larkspur Homes Limited. Reg No 00000000</div>
</footer>

</body>
</html>
```